New Alcoholic Spiked Seltzer Line

We need a can design for a line of low calorie alcoholic seltzer. This product is a sparkling water and vodka drink with no sugar added in a slim 12 oz can.

This is a lighter, healthier, alternative to the sugary ready-to-drinks on the market. The product contains only 3 ingredients: Vodka, Water and Natural Flavors. It has only 100 calories but still has 5% alcohol, so you don't need to sacrifice alcohol to cut calories.

This product also does not contain any preservatives.

We want this design to communicate the following objectives to the consumer and in this order:

1. Appetizing product
2.Low calorie
3.Communicate the type of beverage (Spiked Seltzer)

The brand name of the product is VELKA.

The flavor of the product needed to be used for the design is Mango-Orange.

Comparable products are:

www.brisavelfizz.example/
https://www.tarnowbubble.example
https://quellrind.example/

The designs should not infringe or copy the creative directions of the products mentionned above. They are only given so that you can better understand the type of product we are developing.

Target Market(s)

Young Professional women between the ages of 25 and 44

Industry/Entity Type

Product

Colors

Designer to choose colors to be used in the design.

Requirements
Must have
• Design extendibility, meaning it can be adapted for other flavors.
• This is a new category in the market we are targeting, so consumers must easily be able to identify what type of product this is.

```html
<!DOCTYPE html>
<html lang="en">
<head>
<meta charset="utf-8">
<title>VELKA Spiked Seltzer – Label Line</title>
<link rel="stylesheet" href="https://fonts.googleapis.com/css2?family=Josefin+Sans:wght@300;400&family=Kaushan+Script&family=Dancing+Script:wght@500&family=Questrial&display=swap">
<style>
  :root {
    --page: #ffffff;
    --ink: #111111;
    --label: #ffffff;
    --label-edge: #e4e4e4;
    --orange: #f2561d;
    --orange-deep: #dd5a24;
    --green: #7ed321;
    --green-deep: #76d61e;
    --yellow: #f6e41c;
    --yellow-deep: #f3df12;
    --bubble-a: #d9d9d9;
    --bubble-b: #f2f2f2;
  }
  * { margin: 0; padding: 0; box-sizing: border-box; }
  html, body { width: 1200px; height: 874px; overflow: hidden; background: var(--page); }
  .canvas { position: relative; width: 1200px; height: 874px; background: var(--page); }

  .label {
    position: absolute; top: 114px; width: 242px; height: 646px;
    background: var(--label); border: 1px solid var(--label-edge);
    color: var(--ink);
  }
  .label--orange { left: 170px; --flavor: var(--orange); --band: var(--orange-deep); }
  .label--melon  { left: 478px; --flavor: var(--green);  --band: var(--green-deep); }
  .label--banana { left: 786px; --flavor: var(--yellow); --band: var(--yellow-deep); }

  .band { position: absolute; left: 0; width: 100%; background: var(--band); }
  .band--top { top: 12px; height: 20px; }
  .band--bottom { bottom: 18px; height: 16px; }

  .category {
    position: absolute; top: 82px; width: 100%; text-align: center;
    font-family: "Kaushan Script", cursive; font-size: 19px; letter-spacing: 0.5px;
  }
  .flavor-disc {
    position: absolute; left: 10px; top: 164px; width: 168px; height: 168px;
    border-radius: 50%; background: var(--flavor);
  }
  .brand {
    position: absolute; left: 28px; top: 222px;
    font-family: "Josefin Sans", sans-serif; font-weight: 400;
    font-size: 46px; letter-spacing: 6px; color: var(--ink);
  }
  .brand-mark {
    display: inline-block; width: 10px; height: 10px; border-radius: 50%;
    background: var(--ink); margin-left: 2px; vertical-align: top; margin-top: 6px;
  }
  .bubbles {
    position: absolute; left: 100px; top: 250px; width: 124px; height: 110px;
    border-radius: 50%;
    background: radial-gradient(circle, var(--bubble-a) 0%, var(--bubble-b) 70%, transparent 100%);
  }
  .brush {
    position: absolute; left: 4px; top: 362px; width: 236px; height: 86px;
    background: var(--flavor); border-radius: 40px 6px 30px 10px;
    transform: skewY(-10deg);
  }
  .flavor-name {
    position: absolute; top: 382px; width: 100%; text-align: center;
    font-family: "Josefin Sans", sans-serif; font-weight: 300;
    font-size: 27px; line-height: 26px; letter-spacing: 9px; text-transform: uppercase;
  }
  .facts {
    position: absolute; left: 36px; top: 496px; list-style: disc;
    font-family: "Dancing Script", cursive; font-size: 15px; line-height: 16px;
    letter-spacing: 1px;
  }
  .volume {
    position: absolute; top: 598px; width: 100%; text-align: center;
    font-family: "Questrial", sans-serif; font-size: 12px; line-height: 13px;
  }
</style>
</head>
<body>
<main class="canvas">

  <section class="label label--orange">
    <div class="band band--top"></div>
    <p class="category">SPIKED SELTZER</p>
    <div class="flavor-disc"></div>
    <p class="brand">VELKA<span class="brand-mark"></span></p>
    <div class="bubbles" role="img" aria-label="Cluster of black sparkling bubbles"></div>
    <div class="brush" role="img" aria-label="Orange halftone brush stroke"></div>
    <p class="flavor-name">Orange<br>Mango</p>
    <ul class="facts">
      <li>5% Alcohol by Volume</li>
      <li>100 Calories per Can</li>
      <li>0 Gram of Sugar</li>
      <li>All natural</li>
      <li>Gluten Free</li>
    </ul>
    <p class="volume">12 oz<br>5% Alcohol</p>
    <div class="band band--bottom"></div>
  </section>

  <section class="label label--melon">
    <div class="band band--top"></div>
    <p class="category">SPIKED SELTZER</p>
    <div class="flavor-disc"></div>
    <p class="brand">VELKA<span class="brand-mark"></span></p>
    <div class="bubbles" role="img" aria-label="Cluster of black sparkling bubbles"></div>
    <div class="brush" role="img" aria-label="Green halftone brush stroke"></div>
    <p class="flavor-name">Melon<br>Lime</p>
    <ul class="facts">
      <li>5% Alcohol by Volume</li>
      <li>100 Calories per Can</li>
      <li>0 Gram of Sugar</li>
      <li>All natural</li>
      <li>Gluten Free</li>
    </ul>
    <p class="volume">12 oz<br>5% Alcohol</p>
    <div class="band band--bottom"></div>
  </section>

  <section class="label label--banana">
    <div class="band band--top"></div>
    <p class="category">SPIKED SELTZER</p>
    <div class="flavor-disc"></div>
    <p class="brand">VELKA<span class="brand-mark"></span></p>
    <div class="bubbles" role="img" aria-label="Cluster of black sparkling bubbles"></div>
    <div class="brush" role="img" aria-label="Yellow halftone brush stroke"></div>
    <p class="flavor-name">Banana<br>Citrus</p>
    <ul class="facts">
      <li>5% Alcohol by Volume</li>
      <li>100 Calories per Can</li>
      <li>0 Gram of Sugar</li>
      <li>All natural</li>
      <li>Gluten Free</li>
    </ul>
    <p class="volume">12 oz<br>5% Alcohol</p>
    <div class="band band--bottom"></div>
  </section>

</main>
</body>
</html>
```